Consulting Company needs business card design

We need a business card design for a new consulting and business solutions company based in Bermuda called Corvale Partners Limited. Looking for a double sided business card with one side only including the company logo thats attached and the other including contact information. Logo contains blue and turquoise colors and is fine to be on both sides of the card.
Contact Information for Business Card
Corvale Partners Limited
P.O. Box HM318
Devonshire DV BX
Bermuda
Name: Marcus Pellegrin
Position: Director
Telephone: 1 441 733 4906
Email: mpellegrin@corvale.example
Website: www.corvale.example

```html
<!DOCTYPE html>
<html lang="en">
<head>
<meta charset="utf-8">
<title>Corvale Partners Limited – Business Card</title>
<link rel="stylesheet" href="https://fonts.googleapis.com/css2?family=Noto+Serif&family=Open+Sans:wght@400;600&family=Montserrat:wght@600&display=swap">
<style>
  :root {
    --backdrop: #27272b;
    --card: #ffffff;
    --sky: #4fd3f7;
    --aqua: #4ee6c0;
    --teal-name: #45d2d0;
    --muted: #9aa3a6;
    --ink: #1d1d1d;
    --band: #535e64;
    --rule: #c9cdcf;
  }
  * { margin: 0; padding: 0; box-sizing: border-box; }
  html, body { width: 927px; height: 1200px; overflow: hidden; background: var(--backdrop); }
  .sheet { position: relative; width: 927px; height: 1200px; font-family: "Open Sans", sans-serif; }

  .card { position: absolute; left: 117px; width: 701px; height: 400px; background: var(--card); overflow: hidden; }
  .card--front { top: 188px; }
  .card--back { top: 602px; }

  .corner { position: absolute; top: 0; right: 0; width: 46px; height: 46px; }

  .holder { position: absolute; left: 61px; top: 48px; }
  .holder__name { font-family: "Noto Serif", serif; font-size: 29px; color: var(--teal-name); line-height: 1.1; white-space: nowrap; }
  .holder__role { font-size: 18px; color: var(--muted); margin-left: 10px; margin-top: 2px; }

  .brand { position: absolute; display: flex; align-items: center; gap: 12px; color: var(--sky);
           font-family: "Open Sans", sans-serif; font-weight: 600; white-space: nowrap; }
  .brand__dot { background: var(--sky); flex: none; }
  .brand--small { left: 61px; top: 176px; font-size: 25px; }
  .brand--small .brand__dot { width: 34px; height: 34px; }
  .brand--large { left: 50%; top: 50%; transform: translate(-50%, -62%); font-size: 52px; gap: 20px; }
  .brand--large .brand__dot { width: 64px; height: 64px; }

  .divider { position: absolute; left: 344px; top: 150px; width: 13px; height: 107px; }
  .divider span { position: absolute; top: 0; bottom: 0; width: 1px; background: var(--rule); }
  .divider span:nth-child(1) { left: 0; top: 12px; bottom: 12px; }
  .divider span:nth-child(2) { left: 6px; }
  .divider span:nth-child(3) { left: 12px; top: 12px; bottom: 12px; }

  .address { position: absolute; left: 386px; top: 151px; font-style: normal; white-space: nowrap; }
  .address__company { font-family: "Montserrat", sans-serif; font-weight: 600; font-size: 22px; color: var(--muted); line-height: 1.2; }
  .address__line { font-size: 18.5px; color: var(--ink); line-height: 1.2; }

  .contact-band { position: absolute; left: 0; bottom: 0; width: 100%; height: 70px; background: var(--band);
                  display: flex; align-items: center; justify-content: center; gap: 14px;
                  color: #fff; font-size: 17px; white-space: nowrap; padding: 0 16px; }
  .contact-band span { flex: none; }
  .accent-rule { position: absolute; left: 0; width: 100%; height: 4px; background: linear-gradient(90deg, var(--sky), var(--aqua)); }
  .card--front .accent-rule { bottom: 70px; }
  .card--back .accent-rule { bottom: 0; }
</style>
</head>
<body>
<main class="sheet">

  <section class="card card--front" aria-label="Business card front">
    <svg class="corner" viewBox="0 0 46 46" aria-hidden="true">
      <polygon points="0,0 46,0 46,46" fill="var(--sky)"/>
      <polygon points="0,0 10,0 46,36 46,46" fill="var(--aqua)"/>
    </svg>

    <div class="holder">
      <p class="holder__name">Marcus Pellegrin</p>
      <p class="holder__role">Director</p>
    </div>

    <div class="brand brand--small">
      <span class="brand__dot"></span>
      <span class="brand__name">Corvale Partners</span>
    </div>

    <div class="divider" aria-hidden="true"><span></span><span></span><span></span></div>

    <address class="address">
      <p class="address__company">Corvale Partners Limited</p>
      <p class="address__line">P.O. Box HM318</p>
      <p class="address__line">Devonshire DV BX</p>
      <p class="address__line">Bermuda</p>
    </address>

    <div class="accent-rule"></div>
    <div class="contact-band">
      <span>1. 441. 733 4906</span><span>|</span>
      <span>mpellegrin@corvale.example</span><span>|</span>
      <span>www.corvale.example</span>
    </div>
  </section>

  <section class="card card--back" aria-label="Business card back">
    <svg class="corner" viewBox="0 0 46 46" aria-hidden="true">
      <polygon points="0,0 46,0 46,46" fill="var(--sky)"/>
      <polygon points="0,0 10,0 46,36 46,46" fill="var(--aqua)"/>
    </svg>

    <div class="brand brand--large">
      <span class="brand__dot"></span>
      <span class="brand__name">Corvale Partners</span>
    </div>

    <div class="accent-rule"></div>
  </section>

</main>
</body>
</html>
```